Plumbing and heating business card design

i need a new business card for the company i work for called Dr. Brightpipe. It is a plumbing and heating company that has been operating for over 30 years. We are not like these big plumbing companies that have ways to charge the customer as much as possible. Our company does only what is necessary and what is needed to do the job right the first time without the high cost. we are a neighborhood business which kind of explains why we don't charge customers through the roof. I would like to see a design with a nice background anything but just plain white. maybe like a light blue at the top of the design. on the back of the card i would like it to say " T. Vandermeer's Dr. Brightpipe". maybe add some color to the lettering on the front of the card for example blue font for plumbing and red font for heating. raised print. im sure Cardolux designers will make it look good. The final design should help spread a good word about our company and help grow business.

Industry/Entity Type

Business

Contact Information for Business Card

Dr. Brightpipe, Plumbing & heating, Gordon Tasker, Northeast District Operations manager, 4827 Birchwell st., Office:(555)-284-1937, doctorbrightpipe@mailverra.net

Requirements
Must have
• raised print finish and a nice sturdy feel.

```html
<!DOCTYPE html>
<html lang="en">
<head>
<meta charset="utf-8">
<title>Dr. Brightpipe – Business Card</title>
<link rel="stylesheet" href="https://fonts.googleapis.com/css2?family=Michroma&family=Oswald:wght@400;500&display=swap">
<style>
  :root {
    --page-bg: #ecebe8;
    --card-dark: #141414;
    --card-light: #ffffff;
    --ink: #1f1f1f;
    --ink-light: #f4f4f4;
    --brand-blue: #4aa3dc;
    --brand-red: #e0202a;
    --muted: #9a9a9a;
  }
  * { box-sizing: border-box; margin: 0; padding: 0; }
  html, body {
    width: 1200px; height: 1200px; overflow: hidden;
    background: var(--page-bg);
  }
  .canvas { position: relative; width: 1200px; height: 1200px; }

  .card {
    position: absolute;
    width: 760px; height: 434px;
    border-radius: 4px;
    box-shadow: 0 10px 30px rgba(0,0,0,.18);
    overflow: hidden;
  }

  /* Back of card */
  .card--back {
    left: 120px; top: 110px;
    background: radial-gradient(ellipse at 40% 35%, #262626 0%, var(--card-dark) 70%);
    display: flex; align-items: center; justify-content: center;
  }
  .brand-lockup { display: flex; align-items: center; gap: 26px; }
  .brand-dot {
    width: 22px; height: 22px; border-radius: 50%;
    background: var(--brand-red);
    flex-shrink: 0;
  }
  .brand-text { display: flex; flex-direction: column; gap: 14px; }
  .brand-name {
    font-family: "Michroma", sans-serif;
    font-size: 30px; line-height: 1.35;
    color: var(--ink-light);
  }
  .brand-tagline {
    font-family: "Oswald", sans-serif;
    font-size: 30px; letter-spacing: 3px; text-transform: uppercase;
    color: var(--brand-blue);
  }

  /* Front of card */
  .card--front {
    left: 320px; top: 650px;
    background: var(--card-light);
  }
  .accent-band {
    position: absolute; top: 0; right: 0;
    width: 59%; height: 22px;
    background: var(--brand-blue);
  }
  .front-brand {
    position: absolute; left: 40px; top: 170px; width: 230px;
    display: flex; align-items: center; gap: 12px;
  }
  .front-brand .brand-dot { width: 16px; height: 16px; }
  .front-brand-name {
    font-family: "Michroma", sans-serif;
    font-size: 19px; color: var(--brand-red);
  }
  .divider {
    position: absolute; left: 300px; top: 150px;
    width: 3px; height: 210px;
    background: var(--brand-red);
  }
  .contact { position: absolute; left: 338px; top: 150px; }
  .contact-name {
    font-family: "Michroma", sans-serif;
    font-size: 30px; color: var(--ink); letter-spacing: 1px;
  }
  .contact-title {
    font-family: "Oswald", sans-serif;
    font-size: 22px; color: var(--brand-blue);
    margin-top: 2px; margin-bottom: 18px;
  }
  .contact-list { list-style: none; }
  .contact-item {
    display: flex; align-items: center; gap: 14px;
    font-family: "Oswald", sans-serif; font-weight: 500;
    font-size: 22px; color: var(--ink);
    margin-bottom: 10px;
  }
  .contact-icon { width: 20px; height: 20px; flex-shrink: 0; fill: var(--brand-blue); }
</style>
</head>
<body>
<main class="canvas">

  <section class="card card--back" aria-label="Card back">
    <div class="brand-lockup">
      <span class="brand-dot"></span>
      <div class="brand-text">
        <p class="brand-name">T. Vandermeer's<br>Dr. Brightpipe</p>
        <p class="brand-tagline">Plumbing and Heating</p>
      </div>
    </div>
  </section>

  <section class="card card--front" aria-label="Card front">
    <div class="accent-band"></div>

    <div class="front-brand">
      <span class="brand-dot"></span>
      <span class="front-brand-name">Dr. Brightpipe</span>
    </div>

    <div class="divider"></div>

    <div class="contact">
      <h1 class="contact-name">Gordon Tasker</h1>
      <p class="contact-title">Northeast District Operations manager</p>
      <ul class="contact-list">
        <li class="contact-item">
          <svg class="contact-icon" viewBox="0 0 20 20" aria-hidden="true"><path d="M10 1a6 6 0 0 0-6 6c0 4.5 6 12 6 12s6-7.5 6-12a6 6 0 0 0-6-6zm0 8.3A2.3 2.3 0 1 1 10 4.7a2.3 2.3 0 0 1 0 4.6z"/></svg>
          4827 Birchwell st.,
        </li>
        <li class="contact-item">
          <svg class="contact-icon" viewBox="0 0 20 20" aria-hidden="true"><path d="M2 7c0-2 3.5-3.5 8-3.5S18 5 18 7v1.5h-4V7c-1-.6-2.4-.9-4-.9s-3 .3-4 .9v1.5H2zM4 10h12l1.5 7h-15zm6 1.8a2.2 2.2 0 1 0 0 4.4 2.2 2.2 0 0 0 0-4.4z"/></svg>
          (555)-284-1937
        </li>
        <li class="contact-item">
          <svg class="contact-icon" viewBox="0 0 20 20" aria-hidden="true"><path d="M1 4h18v12H1zm2 2v.4l7 4.6 7-4.6V6zm0 2.8V14h14V8.8l-7 4.6z"/></svg>
          doctorbrightpipe@mailverra.net
        </li>
      </ul>
    </div>
  </section>

</main>
</body>
</html>
```